Corvendal needs a Pet supplement label design

We are Corvendal, a private label company located in California. We private label all natural pet products, mainly supplements and vitamins for dogs and cats of all sizes and breeds. This product is Wild Alaskan Salmon Oil for dogs and cats of all sizes and breeds. The product is a 16 oz bottle of Wild Alaskan Salmon Oil rich in EPA and DHA Omega 3s for dogs and cats (please see picture attached for a picture of what the bottle looks like).
The primary design will be the 16 oz bottle size
The secondary design will be the 32 oz bottle size (only winner will do the 32 oz design).
Size dimensions:
16oz - 8.25 x 4.00 inches (209.55 x 101.6 millimeters)
32oz - 9.8425 x 5.512 inches (250 x 140 millimeters) (only winner will do the 32 oz design)
Information on label:
Center of label:
-please use corvendal logo some place on the front of the label.
- you may add a dog and cat picture on the label design
- you may add dog and cat paw prints on the label design
-you may add picture of a salmon somewhere in the lettering/background or on the bottle
-please choose colors that will go along with the colors of the corvendal logo as well as matching a concept that relates to Salmon Oil.
Name of Brand: Corvendal (see logo attached)
Title of Product: Wild Alaskan Salmon Oil
Rich in EPA and DHA Omega 3 and Omega 6 Fatty Acids.

For Dogs and Cats

Supports and promotes heart health, healthy Skin, glossier coat, joints, healthy immune system, and brain development
All-natural with no preservatives.

Side 1: Left side, About: Corvendal's Wild Caught Alaskan Salmon Oil is made from the body oils of wild caught salmon from the Pacific Ocean in Alaska. Pharmaceutical and human grade in accordance with pharmacopeia. These fish oils are molecularly distilled to remove contaminants such as PCBs, mercury, toxins and metals. Each batch is tested by a third party lab verifying each batch exceeds the stringent quality standards set by California’s proposition 65.

Caution: Not intended for human consumption. Product is for pet consumption only. When unsealed store at room temperature away from light. Refrigerate after opening. Not to be used as a meal replacement.

These statements have not been evaluated by the food and drug administration. This product is not intended to treat, cure or prevent any disease

Still side 1: left side:
Suggested use chart: (compare to other product's charts as displayed in the photos attached. serving size amounts per weight are the same).
Add on top of your pets food and mix
body weight: pump strokes:
up to 12 lbs 1/2
12-25 lbs 1
25-50 lbs 2
50-75 lbs 3
over 75 lbs 4

Side 2: Right side
Nutritional Info Chart: per serving (5ml or 1 tsp)
Total fat (g) (TBA)
Saturated (g) (TBA)
Monounsaturated (g) (TBA)
Polyunsaturated (g) (TBA)
*Total omega 3 (mg) 1,227
*EPA (mg) 423
*DHA (mg) 465
*Not recognized as an essential nutrient by the AAFCO.

Dog Food nutrient profile

Guaranteed analysis chart:
per serving (5ml or 1 tsp)
Crude Fat 99.9 % (min)
Moisture .1 % (max)
*Omega 3 Fatty acids 30% (min)
*DHA 11% (min)
*EPA 10% (min)
*Other Omega 3 5.0 % (min)
*Omega-6 Fatty Acids 4.0 % (min)
* Not recognized as an essential nutrient by the AAFCO.

Dog Food nutrient profile

Ingredients: Wild Caught Alaskan Salmon Oil, all-natural non GMO Vitamin E

Made in USA logo, All natural ingredients logo
( I have attached all natural and human grade logos below). Please use if you can find image on account such as pixelbarn or photovaultix.

Add sku number: K774QB2R5T Create barcode for sku number (may be done after winner is selected)

Add anywhere on bottle:
Health benefits of Omega 3 fish oil for pets:
supports cardiovascular health, joints, brain development, immune system, eyes, healthy skin and shin coat, relief from dry itchy skin, overall health and vitality.

Distributed by:
CORVENDAL
872 N. BRISKET HILL RD. #214-958
SAN MARCOS, CA 92143
www.corvendalpetcare.example

* I attached several examples in the photos below of other wild salmon oil to give you an idea of what other projects look like.
Updates

Target Market(s)

Cats and Dogs of all ages, sizes and breeds.

Industry/Entity Type

It Company

Colors

Designer to choose colors to be used in the design.

Requirements
Must have
• All or majority of the included items listed in the project description
Nice to have
• Please blend the design of the label to where it will match the colors of the corvendal logo. Add any additional colors you think will go well.

```html
<!DOCTYPE html>
<html lang="en">
<head>
<meta charset="utf-8">
<title>Corvendal Wild Alaskan Salmon Oil – Label Options</title>
<link rel="stylesheet" href="https://fonts.googleapis.com/css2?family=Anton&family=Archivo+Narrow:wght@400;700&family=Roboto:wght@300&display=swap">
<style>
  :root {
    --canvas: #ffffff;
    --ink: #2f2a88;
    --ink-dark: #1f1b5e;
    --brand: #3b2c1c;
    --caption: #6d6d6d;
    --orange: #f07d1a;
    --orange-deep: #e4621a;
    --amber: #f6a91c;
    --yellow: #fbd23a;
    --sky: #2a9ad6;
    --sky-deep: #1b6fb5;
    --lime: #b4d64a;
    --green: #6fb43a;
    --cream: #f8f2dc;
  }
  * { box-sizing: border-box; margin: 0; padding: 0; }
  html, body { width: 1200px; height: 873px; overflow: hidden; background: var(--canvas); }
  .lineup { position: relative; width: 1200px; height: 873px; }

  .label {
    position: absolute; top: 362px; width: 192px; height: 318px;
    overflow: hidden; text-align: center; color: var(--ink);
    font-family: "Archivo Narrow", "Arial Narrow", sans-serif;
  }
  .label--sunset  { left: 47px;  background: linear-gradient(180deg, var(--orange) 0%, var(--amber) 45%, var(--sky) 100%); }
  .label--meadow  { left: 273px; background: radial-gradient(circle at 50% 30%, #eef6b8 0%, var(--lime) 55%, var(--green) 100%); }
  .label--sunrise { left: 522px; background: radial-gradient(circle at 50% 32%, #fff6b0 0%, var(--yellow) 35%, var(--amber) 70%, var(--orange) 100%); }
  .label--ocean   { left: 745px; background: radial-gradient(circle at 50% 40%, #ffffff 0%, #bfe6f7 25%, var(--sky) 60%, var(--sky-deep) 100%); }
  .label--ember   { left: 968px; background: radial-gradient(circle at 50% 35%, var(--amber) 0%, var(--orange) 55%, var(--orange-deep) 100%); }

  .banner {
    position: absolute; left: 50%; top: 0; width: 84px; height: 100px;
    transform: translateX(-50%); background: var(--cream);
    clip-path: polygon(0 0, 100% 0, 100% 88%, 50% 100%, 0 88%);
  }
  .brand {
    position: absolute; left: 0; right: 0; top: 30px;
    display: flex; flex-direction: column; align-items: center; gap: 4px;
  }
  .brand__mark { width: 46px; height: 46px; border-radius: 50%; background: var(--cream); border: 2px solid var(--green); }
  .brand__name { font-size: 9px; font-weight: 700; letter-spacing: .08em; color: var(--brand); }

  .salmon-art {
    position: absolute; left: 8px; right: 8px; top: 128px; height: 70px;
    border-radius: 50%; background: radial-gradient(ellipse at center, rgba(255,255,255,.35), rgba(255,255,255,0) 70%);
  }

  .title { position: absolute; left: 0; right: 0; top: 128px; }
  .title__kicker { font-weight: 700; font-size: 11px; letter-spacing: .02em; color: var(--ink); }
  .title__main {
    font-family: "Anton", "Impact", sans-serif; font-size: 32px; line-height: 30px;
    color: var(--ink); text-shadow: 0 0 3px #fff, 0 0 2px #fff;
  }
  .title__sub {
    display: flex; align-items: center; justify-content: center; gap: 6px;
    font-family: "Anton", "Impact", sans-serif; font-size: 25px; line-height: 26px;
    color: var(--ink); text-shadow: 0 0 3px #fff;
  }
  .title__sub::before, .title__sub::after { content: ""; width: 38px; height: 2px; background: var(--ink); }

  .copy { position: absolute; left: 8px; right: 8px; top: 222px; color: var(--ink-dark); }
  .copy__lead { font-weight: 700; font-size: 10.5px; line-height: 12px; color: var(--ink); }
  .copy__for { margin-top: 5px; font-size: 7.5px; font-weight: 700; }
  .copy__body { font-size: 6px; line-height: 7.2px; font-weight: 700; }
  .copy__net { margin-top: 5px; font-size: 8px; font-weight: 700; line-height: 10px; }

  .caption {
    position: absolute; top: 736px; width: 60px; margin-left: -30px; text-align: center;
    font-family: "Roboto", Arial, sans-serif; font-weight: 300; font-size: 24px; color: var(--caption);
  }
</style>
</head>
<body>
<main class="lineup">

  <section class="label label--sunset">
    <div class="banner"></div>
    <div class="brand"><span class="brand__mark"></span><span class="brand__name">CORVENDAL</span></div>
    <div class="salmon-art" role="img" aria-label="Leaping salmon illustration behind the title"></div>
    <div class="title"><p class="title__kicker">WILD ALASKAN</p><p class="title__main">SALMON</p><p class="title__sub">OIL</p></div>
    <div class="copy">
      <p class="copy__lead">Rich in EPA and DHA Omega 3 and Omega 6 Fatty Acids.</p>
      <p class="copy__for">for DOGS &amp; CATS</p>
      <p class="copy__body">Supports and promotes heart health, healthy Skin, glossier coat, joints, healthy immune system, and brain development All-natural with no preservatives</p>
      <p class="copy__net">Net 16FL oZ / 473 ml<br>Dietary Supplement</p>
    </div>
  </section>

  <section class="label label--meadow">
    <div class="brand"><span class="brand__mark"></span><span class="brand__name">CORVENDAL</span></div>
    <div class="salmon-art" role="img" aria-label="Salmon illustration and paw prints behind the title"></div>
    <div class="title"><p class="title__kicker">WILD ALASKAN</p><p class="title__main">SALMON</p><p class="title__sub">OIL</p></div>
    <div class="copy">
      <p class="copy__lead">Rich in EPA and DHA Omega 3 and Omega 6 Fatty Acids.</p>
      <p class="copy__for">for DOGS &amp; CATS</p>
      <p class="copy__body">Supports and promotes heart health, healthy Skin, glossier coat, joints, healthy immune system, and brain development All-natural with no preservatives</p>
      <p class="copy__net">Net 16FL oZ / 473 ml<br>Dietary Supplement</p>
    </div>
  </section>

  <section class="label label--sunrise">
    <div class="brand"><span class="brand__mark"></span><span class="brand__name">CORVENDAL</span></div>
    <div class="salmon-art" role="img" aria-label="Sunburst with salmon illustration behind the title"></div>
    <div class="title"><p class="title__kicker">WILD ALASKAN</p><p class="title__main">SALMON</p><p class="title__sub">OIL</p></div>
    <div class="copy">
      <p class="copy__lead">Rich in EPA and DHA Omega 3 and Omega 6 Fatty Acids.</p>
      <p class="copy__for">for DOGS &amp; CATS</p>
      <p class="copy__body">Supports and promotes heart health, healthy Skin, glossier coat, joints, healthy immune system, and brain development All-natural with no preservatives</p>
      <p class="copy__net">Net 16FL oZ / 473 ml<br>Dietary Supplement</p>
    </div>
  </section>

  <section class="label label--ocean">
    <div class="brand"><span class="brand__mark"></span><span class="brand__name">CORVENDAL</span></div>
    <div class="salmon-art" role="img" aria-label="Blue sunburst with salmon illustration behind the title"></div>
    <div class="title"><p class="title__kicker">WILD ALASKAN</p><p class="title__main">SALMON</p><p class="title__sub">OIL</p></div>
    <div class="copy">
      <p class="copy__lead">Rich in EPA and DHA Omega 3 and Omega 6 Fatty Acids.</p>
      <p class="copy__for">for DOGS &amp; CATS</p>
      <p class="copy__body">Supports and promotes heart health, healthy Skin, glossier coat, joints, healthy immune system, and brain development All-natural with no preservatives.</p>
      <p class="copy__net">Net 16FL oZ / 473 ml<br>Dietary Supplement</p>
    </div>
  </section>

  <section class="label label--ember">
    <div class="brand"><span class="brand__mark"></span><span class="brand__name">CORVENDAL</span></div>
    <div class="salmon-art" role="img" aria-label="Salmon illustration and paw prints behind the title"></div>
    <div class="title"><p class="title__kicker">WILD ALASKAN</p><p class="title__main">SALMON</p><p class="title__sub">OIL</p></div>
    <div class="copy">
      <p class="copy__lead">Rich in EPA and DHA Omega 3 and Omega 6 Fatty Acids.</p>
      <p class="copy__for">for DOGS &amp; CATS</p>
      <p class="copy__body">Supports and promotes heart health, healthy Skin, glossier coat, joints, healthy immune system, and brain development All-natural with no preservatives.</p>
      <p class="copy__net">Net 16FL oZ / 473 ml<br>Dietary Supplement</p>
    </div>
  </section>

  <p class="caption" style="left:148px">01</p>
  <p class="caption" style="left:376px">02</p>
  <p class="caption" style="left:613px">03</p>
  <p class="caption" style="left:848px">04</p>
  <p class="caption" style="left:1066px">05</p>

</main>
</body>
</html>
```